Brownie Snack Packaging

Design the film wrapper packaging for a brownie snack. It needs to be cohesive with our existing product line (please review attached photos), but still differentiated from it to avoid customer confusion.
Brief is outlined in the images attached. Please review prior to submitting designs. All designs should have the iridescent white pearl packaging color, with the text:
High Protein Brownie
10g Protein
Vegan
Gluten-Free
No Added Sugars
We would like to see designs with square packaging with a mouth-watering brownie image being the most prominent. Logo of brand "ORUNE" should be in upper right corner.
Note: we have another product line of cashew butter sachets that are pink, blue, & chocolate - I'm attaching those for reference so you can design these brownies to look somewhat related to the cashew butters.
Look and feel
Each slider illustrates characteristics of the customer's brand and the style your logo design should communicate.

```html
<!DOCTYPE html>
<html lang="en">
<head>
<meta charset="utf-8">
<title>ORUNE High Protein Brownie – Wrapper Front</title>
<link rel="stylesheet" href="https://fonts.googleapis.com/css2?family=Abril+Fatface&family=Josefin+Sans:wght@400&family=Passion+One:wght@400&family=Roboto+Condensed:wght@400&display=swap">
<style>
  :root {
    --stage: #3d3d3d;
    --pearl: #ffffff;
    --gold: #8c7452;
    --caramel: #9a6b45;
    --cocoa-dark: #2a0f0a;
    --bar: #2a0c08;
    --divider: #c9a983;
    --text-light: #ffffff;
    --photo-deep: #3b1c10;
    --photo-mid: #6b3a22;
  }
  * { margin: 0; padding: 0; box-sizing: border-box; }
  html, body {
    width: 764px; height: 1200px; overflow: hidden;
    background: var(--stage);
  }
  .wrapper-front {
    position: absolute;
    left: 62px; top: 238px;
    width: 640px; height: 724px;
    background: var(--pearl);
    overflow: hidden;
  }
  .brand-name {
    position: absolute;
    top: 56px; left: 0; width: 100%;
    text-align: center;
    font-family: "Josefin Sans", sans-serif;
    font-weight: 400;
    font-size: 70px;
    letter-spacing: 4px;
    line-height: 1;
    color: var(--gold);
  }
  .protein-ribbon {
    position: absolute;
    left: 201px; top: 149px;
    width: 237px; height: 44px;
  }
  .protein-ribbon svg { position: absolute; inset: 0; }
  .protein-ribbon span {
    position: relative;
    display: block;
    text-align: center;
    font-family: "Passion One", sans-serif;
    font-size: 33px;
    line-height: 44px;
    color: var(--text-light);
  }
  .product-name {
    position: absolute;
    top: 150px; left: 0; width: 100%;
    text-align: center;
    font-family: "Abril Fatface", serif;
    font-size: 112px;
    line-height: 1;
    color: var(--cocoa-dark);
  }
  .claims-bar {
    position: absolute;
    left: 94px; top: 278px;
    width: 457px; height: 48px;
    background: var(--bar);
    display: flex;
    align-items: center;
  }
  .claim {
    font-family: "Roboto Condensed", sans-serif;
    font-size: 14px;
    line-height: 15px;
    color: var(--text-light);
    text-align: center;
    height: 38px;
    display: flex; align-items: center; justify-content: center;
  }
  .claim + .claim { border-left: 2px solid var(--divider); }
  .claim--sugar { width: 136px; }
  .claim--vegan { width: 83px; }
  .claim--gluten { width: 90px; }
  .claim--protein { width: 148px; }
  .hero-photo {
    position: absolute;
    left: 0; top: 344px;
    width: 640px; height: 380px;
    background:
      radial-gradient(ellipse 46% 30% at 50% 42%, var(--photo-mid) 0%, var(--photo-deep) 60%, rgba(59,28,16,0) 100%),
      radial-gradient(ellipse 58% 52% at 52% 52%, rgba(59,28,16,0.55) 0%, rgba(59,28,16,0) 100%);
  }
  .net-weight {
    position: absolute;
    right: 26px; top: 682px;
    font-family: "Roboto Condensed", sans-serif;
    font-size: 16px;
    color: var(--cocoa-dark);
  }
</style>
</head>
<body>
  <main class="wrapper-front">
    <div class="brand-name">ORUNE</div>

    <div class="protein-ribbon">
      <svg width="237" height="44" viewBox="0 0 237 44" aria-hidden="true">
        <polygon points="0,0 237,0 222,22 237,44 0,44 15,22" fill="var(--caramel)"/>
      </svg>
      <span>High Protein</span>
    </div>

    <h1 class="product-name">Brownie</h1>

    <div class="claims-bar">
      <div class="claim claim--sugar">No Added<br>Sugars</div>
      <div class="claim claim--vegan">Vegan</div>
      <div class="claim claim--gluten">Gluten<br>Free</div>
      <div class="claim claim--protein">10g Protein</div>
    </div>

    <div class="hero-photo" role="img" aria-label="Photo of a brownie slice drizzled with chocolate sauce"></div>

    <div class="net-weight">Net wt 2 oz (50g)</div>
  </main>
</body>
</html>
```